Business Cards for a small business advisory (business services)

Professional look. Same as would apply for a lawyer, accountant, or other financial services professional. Please use the logo colors

Target Market(s)

small business owners

Industry/Entity Type

Financial Servics

Contact Information for Business Card

Name: Gavin L. Whitmore, CAIA / Title: Business Advisor / Office #: (718) 294-7716 / Mobile #: (917) 382-5047 / Email: g.whitmore@clearfieldventurepartners.example / Web: www.clearfieldventurepartners.example

Font styles to use
Sans Serif

```html
<!DOCTYPE html>
<html lang="en">
<head>
<meta charset="utf-8">
<title>Clearfield Venture Partners – Business Card</title>
<link rel="stylesheet" href="https://fonts.googleapis.com/css2?family=Arimo:wght@400;700&family=Montserrat:wght@700&display=swap">
<style>
  :root {
    --navy: #1a3a6b;
    --green: #8cc63f;
    --white: #ffffff;
    --canvas: #eef0f3;
    --ink: #1a3a6b;
  }
  * { margin: 0; padding: 0; box-sizing: border-box; }
  html, body { width: 1200px; height: 1200px; overflow: hidden; }
  body { background: var(--canvas); position: relative; font-family: "Arimo", Arial, sans-serif; }

  .card {
    position: absolute;
    left: 172px;
    width: 856px;
    height: 500px;
    background: var(--white);
    overflow: hidden;
  }
  .card--front { top: 85px; }
  .card--back { top: 631px; }

  .card__bands { position: absolute; inset: 0; width: 100%; height: 100%; }

  .brand { position: absolute; display: flex; align-items: center; font-family: "Montserrat", sans-serif; }
  .brand__dot { border-radius: 50%; background: var(--navy); flex: none; }
  .brand__name { font-weight: 700; line-height: 1; letter-spacing: -0.5px; color: var(--navy); white-space: nowrap; }

  .card--front .brand { left: 68px; top: 72px; }
  .card--front .brand__dot { width: 52px; height: 52px; margin-right: 16px; }
  .card--front .brand__name { font-size: 42px; }

  .holder {
    position: absolute;
    left: 66px;
    top: 248px;
    font-weight: 700;
    font-size: 35px;
    color: var(--ink);
    white-space: nowrap;
  }
  .holder__credential { font-weight: 400; font-size: 24px; }

  .contact {
    position: absolute;
    right: 67px;
    top: 318px;
    list-style: none;
    color: var(--white);
    font-size: 21px;
  }
  .contact__item {
    display: flex;
    justify-content: flex-end;
    align-items: center;
    height: 33px;
    white-space: nowrap;
  }
  .contact__icon { width: 16px; height: 16px; margin-left: 18px; flex: none; }

  .card--back .brand {
    left: 0; right: 0; top: 0; bottom: 0;
    justify-content: center;
  }
  .card--back .brand__dot { width: 80px; height: 80px; margin-right: 22px; }
  .card--back .brand__name { font-size: 62px; }
</style>
</head>
<body>

  <section class="card card--front" aria-label="Card front">
    <svg class="card__bands" viewBox="0 0 856 500" aria-hidden="true">
      <polygon points="512,262 856,262 856,282 492,282" fill="var(--green)"/>
      <polygon points="0,309 470,309 446,329 0,329" fill="var(--green)"/>
      <polygon points="484,282 856,282 856,500 0,500 0,329 425,329" fill="var(--navy)"/>
      <polygon points="59,444 259,444 315,500 0,500" fill="var(--green)"/>
    </svg>

    <div class="brand">
      <span class="brand__dot"></span>
      <span class="brand__name">Clearfield Partners</span>
    </div>

    <h1 class="holder">Gavin L. Whitmore<span class="holder__credential">, CAIA</span></h1>

    <ul class="contact">
      <li class="contact__item">(718) 294-7716
        <svg class="contact__icon" viewBox="0 0 16 16" aria-hidden="true"><path d="M3.5 1.5l2.3 2.6-1.2 1.8c.8 1.8 2.2 3.2 4 4l1.8-1.2 2.6 2.3-1.3 2.2c-5.3-.4-9.3-4.4-9.7-9.7z" fill="var(--white)"/></svg>
      </li>
      <li class="contact__item">(917) 382-5047
        <svg class="contact__icon" viewBox="0 0 16 16" aria-hidden="true"><rect x="4" y="1" width="8" height="14" rx="1.5" fill="none" stroke="var(--white)" stroke-width="1.4"/><circle cx="8" cy="12.5" r="0.9" fill="var(--white)"/></svg>
      </li>
      <li class="contact__item">g.whitmore@clearfieldventurepartners.example
        <svg class="contact__icon" viewBox="0 0 16 16" aria-hidden="true"><rect x="1" y="3" width="14" height="10" rx="1" fill="var(--white)"/><path d="M1.5 3.8L8 9l6.5-5.2" fill="none" stroke="var(--navy)" stroke-width="1.2"/></svg>
      </li>
      <li class="contact__item">www.clearfieldventurepartners.example
        <svg class="contact__icon" viewBox="0 0 16 16" aria-hidden="true"><circle cx="8" cy="8" r="6.5" fill="none" stroke="var(--white)" stroke-width="1.3"/><ellipse cx="8" cy="8" rx="2.8" ry="6.5" fill="none" stroke="var(--white)" stroke-width="1.1"/><path d="M1.5 8h13M2.6 4.8h10.8M2.6 11.2h10.8" stroke="var(--white)" stroke-width="1"/></svg>
      </li>
    </ul>
  </section>

  <section class="card card--back" aria-label="Card back">
    <div class="brand">
      <span class="brand__dot"></span>
      <span class="brand__name">Clearfield Partners</span>
    </div>
  </section>

</body>
</html>
```